OBW Crestmark Shipping Limited

We need the buissnes card to be very exclusive. As we are all young in our company. We need this to be the gate to make our clients feel deep interest for us.

We are focused in as International Trade advisors, and our products go from Oil Tanker Ships to Rubber balls for dogs.

Our Slogan is Trade Made Near.
And our main marketing will be through Internet.

We were stablished in 2009 In Mexico and we also have offices in Hong Kong.
We have representatives in China and Europe.

Target Market(s)

Is every company or Individual that wants to develop an International Project or product development or Logistic service of Goods and people.
Some of our current projects are Ship Brokerage, Mine Brokerage, Real State and Product Pormotional development.

Industry/Entity Type

It Company

Requirements
Must have
• Our Logo and slogan, and make the card accoriding to the logo.
Nice to have
• Our Colors

```html
<!DOCTYPE html>
<html lang="en">
<head>
<meta charset="utf-8">
<title>OBW Crestmark Shipping Limited – Business Card</title>
<link href="https://fonts.googleapis.com/css2?family=Questrial&family=Tinos&display=swap" rel="stylesheet">
<style>
  :root {
    --bg: #e4e4e2;
    --card: #ffffff;
    --card-shade: #eeeeee;
    --green: #8cc63f;
    --blue: #1a9ad6;
    --navy: #2e3a93;
    --ink: #2b2b2b;
    --muted: #6a6a6a;
    --rule: #b9b9b9;
    --disc: #d7ecf7;
  }
  * { margin: 0; padding: 0; box-sizing: border-box; }
  html, body { width: 1200px; height: 871px; overflow: hidden; background: var(--bg); }
  .stage {
    width: 1200px; height: 871px;
    display: flex; align-items: center; justify-content: center; gap: 60px;
  }
  .card {
    position: relative; width: 520px; height: 297px; overflow: hidden;
    background: linear-gradient(135deg, var(--card) 40%, var(--card-shade));
    box-shadow: 0 6px 18px rgba(0,0,0,.18);
    font-family: "Questrial", "Century Gothic", sans-serif;
  }

  /* Front */
  .front-brand { position: absolute; left: 50px; top: 108px; }
  .front-name { color: var(--navy); font-size: 56px; line-height: 1; letter-spacing: 2px; }
  .front-slogan { color: var(--muted); font-size: 15px; margin-top: 10px; letter-spacing: .5px; }
  .front-disc {
    position: absolute; right: 45px; top: 73px;
    width: 150px; height: 150px; border-radius: 50%;
    background: var(--disc);
  }

  /* Back */
  .holder { position: absolute; left: 42px; top: 36px; }
  .holder-name { font-family: "Tinos", "Times New Roman", serif; font-size: 17px; color: var(--ink); }
  .holder-title { color: var(--green); font-size: 12px; margin-top: 2px; }
  .divider { position: absolute; left: 150px; top: 128px; width: 230px; height: 1px; background: var(--rule); }
  .back-brand {
    position: absolute; right: 34px; top: 62px;
    display: flex; align-items: center; gap: 8px;
  }
  .back-disc { width: 34px; height: 34px; border-radius: 50%; background: var(--disc); }
  .back-name { color: var(--navy); font-size: 24px; letter-spacing: 1px; line-height: 1; }
  .address {
    position: absolute; left: 42px; top: 150px;
    font-style: normal; font-size: 11px; line-height: 18px; color: var(--ink);
  }
  .contacts { position: absolute; left: 320px; top: 146px; list-style: none; font-size: 12px; color: var(--ink); }
  .contacts li { display: flex; align-items: center; gap: 12px; height: 20px; }
  .contacts svg { width: 11px; height: 11px; fill: var(--navy); }
  .swoosh { position: absolute; left: 0; bottom: 0; width: 520px; height: 60px; }
</style>
</head>
<body>
<main class="stage">

  <section class="card card-front" aria-label="Card front">
    <div class="front-brand">
      <div class="front-name">OBW</div>
      <div class="front-slogan">Trade Made Near</div>
    </div>
    <div class="front-disc" aria-hidden="true"></div>
  </section>

  <section class="card card-back" aria-label="Card back">
    <div class="holder">
      <div class="holder-name">Daniel R. Whitmore</div>
      <div class="holder-title">President</div>
    </div>
    <div class="divider"></div>
    <div class="back-brand">
      <div class="back-disc" aria-hidden="true"></div>
      <div class="back-name">OBW</div>
    </div>
    <address class="address">
      4470 W. Harbor Ave. Ste. 210<br>Tempe, Az. 85281
    </address>
    <ul class="contacts">
      <li><svg viewBox="0 0 12 12"><path d="M1 4c0-2 2-3 5-3s5 1 5 3v1H8V4H4v1H1zM3 6h6l2 5H1z"/></svg>480-555-0142</li>
      <li><svg viewBox="0 0 12 12"><path d="M3 1h6v3H3zM1 5h10v6H1zM3 7h2v1H3z"/></svg>480-555-0147</li>
      <li><svg viewBox="0 0 12 12"><path d="M1 2h10v1L6 7 1 3zM1 4.5l5 4 5-4V10H1z"/></svg>daniel@obw.com</li>
      <li><svg viewBox="0 0 12 12"><circle cx="6" cy="6" r="5"/></svg>www.obw.com</li>
    </ul>
    <svg class="swoosh" viewBox="0 0 520 60" preserveAspectRatio="none" aria-hidden="true">
      <path d="M0 8 C120 4 200 40 330 46 C420 50 480 42 520 40 L520 60 L0 60Z" fill="var(--green)"/>
      <path d="M0 4 C120 0 200 36 330 42 C420 46 480 38 520 36 L520 40 C480 42 420 50 330 46 C200 40 120 4 0 8Z" fill="var(--navy)"/>
      <path d="M0 18 C130 14 210 50 340 54 C430 56 490 52 520 50 L520 60 L0 60Z" fill="#ffffff" opacity=".25"/>
    </svg>
  </section>

</main>
</body>
</html>
```